3 App Screens Designed

I have a laundry app and the developers want 3 images to replace the standard 3 attached.

The images should be custom made with a laundry theme and NOT downloaded from an image site

The app background will be white and the images I need to submit must be 1024 x 1024 with transparent background.

NOTE: I only need the images and not the app face.

Thanks

Colors
0054AA
0677BA
7BADD7
CADEEF
E8F1F8

```html
<!DOCTYPE html>
<html lang="en">
<head>
<meta charset="utf-8">
<title>Laundry App Onboarding Screens</title>
<link rel="stylesheet" href="https://fonts.googleapis.com/css2?family=Outfit:wght@500;600&family=Arimo:wght@400&family=Inter:wght@500&display=swap">
<style>
  :root {
    --blue-deep: #0054AA;
    --blue-mid: #0677BA;
    --blue-soft: #7BADD7;
    --blue-pale: #CADEEF;
    --blue-mist: #E8F1F8;
    --bg-light: #D5EAF7;
    --bg-sky: #84C4EA;
    --bg-sky-dark: #71B9E5;
    --bg-sea-light: #BFE0F3;
    --bg-sea: #6CB9E6;
    --text-body: #3d5c7a;
    --ink: #111111;
    --dot-idle: #c9ced6;
    --white: #ffffff;
  }
  * { box-sizing: border-box; margin: 0; padding: 0; }
  html, body { width: 1200px; height: 864px; overflow: hidden; background: var(--white); }
  .canvas { position: relative; width: 1200px; height: 864px; overflow: hidden; background: var(--white); }
  .backdrop { position: absolute; inset: 0; width: 1200px; height: 864px; }

  .screen {
    position: absolute; top: 152px; width: 259px; height: 560px;
    background: var(--white); border-radius: 16px;
    box-shadow: 0 4px 18px rgba(6, 119, 186, 0.10);
  }
  .screen--pickup { left: 163px; }
  .screen--driver { left: 470px; }
  .screen--deliver { left: 778px; }

  .status-bar { position: absolute; top: 9px; left: 22px; right: 11px; height: 16px; display: flex; justify-content: space-between; align-items: center; }
  .status-time { font-family: "Inter", sans-serif; font-weight: 500; font-size: 10px; color: var(--ink); }
  .status-icons { display: block; }

  .illustration {
    position: absolute; left: 55px; top: 76px; width: 150px; height: 222px;
    border-radius: 75px 75px 75px 75px / 110px 110px 75px 75px;
    background: linear-gradient(180deg, var(--blue-mist) 0%, var(--blue-pale) 55%, var(--blue-soft) 100%);
  }

  .screen-title {
    position: absolute; left: 10px; right: 10px; top: 336px;
    font-family: "Outfit", sans-serif; font-weight: 600; font-size: 15px; line-height: 25px;
    color: var(--blue-mid); text-align: center; letter-spacing: 0.1px;
  }
  .screen-copy {
    position: absolute; left: 14px; right: 14px; top: 398px;
    font-family: "Arimo", sans-serif; font-size: 10.5px; line-height: 17.5px;
    color: var(--text-body); text-align: center;
  }
  .screen-title--single { top: 336px; }
  .screen-copy--three { top: 377px; }

  .pager { position: absolute; left: 21px; top: 512px; display: flex; align-items: center; gap: 4.5px; }
  .pager-dot { width: 3.5px; height: 3.5px; border-radius: 50%; background: var(--dot-idle); }
  .pager-dot--active { width: 6.5px; height: 6.5px; background: var(--blue-deep); }

  .tour-action {
    position: absolute; right: 21px; top: 506px;
    font-family: "Outfit", sans-serif; font-weight: 500; font-size: 11px; color: var(--blue-deep);
  }
  .home-indicator { position: absolute; left: 83px; top: 551px; width: 93px; height: 3px; border-radius: 2px; background: var(--ink); }
</style>
</head>
<body>
<div class="canvas">
  <svg class="backdrop" viewBox="0 0 2268 1633" preserveAspectRatio="none" aria-hidden="true">
    <path d="M0,0 H440 L740,300 L310,535 Q200,540 120,460 L0,340 Z" fill="var(--bg-light)"/>
    <path d="M910,0 H1330 L1040,290 Q980,345 880,348 L800,340 L680,235 Z" fill="var(--bg-sky)"/>
    <path d="M440,0 H910 L680,235 Z" fill="var(--bg-sky-dark)"/>
    <path d="M1050,1633 L1380,1300 Q1420,1283 1480,1283 L1640,1346 L1930,1633 Z" fill="var(--bg-sea-light)"/>
    <path d="M1570,1633 L1960,1243 Q2060,1158 2140,1158 Q2220,1160 2268,1195 V1633 Z" fill="var(--bg-sea)" opacity="0.9"/>
  </svg>

  <section class="screen screen--pickup">
    <div class="status-bar">
      <span class="status-time">9:41</span>
      <svg class="status-icons" width="46" height="9" viewBox="0 0 46 9" aria-hidden="true">
        <rect x="0" y="6" width="2" height="3" fill="#111"/><rect x="3" y="4.5" width="2" height="4.5" fill="#111"/><rect x="6" y="3" width="2" height="6" fill="#111"/><rect x="9" y="1" width="2" height="8" fill="#111"/>
        <path d="M14,3.5 Q19,-0.5 24,3.5 M15.8,5.3 Q19,2.8 22.2,5.3" stroke="#111" stroke-width="1.3" fill="none"/><circle cx="19" cy="7.5" r="1.2" fill="#111"/>
        <rect x="29" y="1" width="14" height="7" rx="2" fill="#111"/><rect x="44" y="3.5" width="1.2" height="2" fill="#111"/>
      </svg>
    </div>
    <div class="illustration" role="img" aria-label="Illustration of a location pin with a clock and a hand tapping a calendar date, set in a water drop"></div>
    <h2 class="screen-title">Select a Convenient Pickup<br>Date and Time.</h2>
    <p class="screen-copy">We can collect from your home, office or<br>wherever works for you.</p>
    <div class="pager"><span class="pager-dot pager-dot--active"></span><span class="pager-dot"></span><span class="pager-dot"></span></div>
    <span class="tour-action">Skip Tour</span>
    <span class="home-indicator"></span>
  </section>

  <section class="screen screen--driver">
    <div class="status-bar">
      <span class="status-time">9:41</span>
      <svg class="status-icons" width="46" height="9" viewBox="0 0 46 9" aria-hidden="true">
        <rect x="0" y="6" width="2" height="3" fill="#111"/><rect x="3" y="4.5" width="2" height="4.5" fill="#111"/><rect x="6" y="3" width="2" height="6" fill="#111"/><rect x="9" y="1" width="2" height="8" fill="#111"/>
        <path d="M14,3.5 Q19,-0.5 24,3.5 M15.8,5.3 Q19,2.8 22.2,5.3" stroke="#111" stroke-width="1.3" fill="none"/><circle cx="19" cy="7.5" r="1.2" fill="#111"/>
        <rect x="29" y="1" width="14" height="7" rx="2" fill="#111"/><rect x="44" y="3.5" width="1.2" height="2" fill="#111"/>
      </svg>
    </div>
    <div class="illustration" role="img" aria-label="Illustration of a driver carrying a blue laundry basket, set in a water drop"></div>
    <h2 class="screen-title">Your Driver Will Come and<br>Pick Them Up</h2>
    <p class="screen-copy">Your items will then be processed according<br>to the specifications you noted in the app.</p>
    <div class="pager"><span class="pager-dot"></span><span class="pager-dot pager-dot--active"></span><span class="pager-dot"></span></div>
    <span class="tour-action">Skip Tour</span>
    <span class="home-indicator"></span>
  </section>

  <section class="screen screen--deliver">
    <div class="status-bar">
      <span class="status-time">9:41</span>
      <svg class="status-icons" width="46" height="9" viewBox="0 0 46 9" aria-hidden="true">
        <rect x="0" y="6" width="2" height="3" fill="#111"/><rect x="3" y="4.5" width="2" height="4.5" fill="#111"/><rect x="6" y="3" width="2" height="6" fill="#111"/><rect x="9" y="1" width="2" height="8" fill="#111"/>
        <path d="M14,3.5 Q19,-0.5 24,3.5 M15.8,5.3 Q19,2.8 22.2,5.3" stroke="#111" stroke-width="1.3" fill="none"/><circle cx="19" cy="7.5" r="1.2" fill="#111"/>
        <rect x="29" y="1" width="14" height="7" rx="2" fill="#111"/><rect x="44" y="3.5" width="1.2" height="2" fill="#111"/>
      </svg>
    </div>
    <div class="illustration" role="img" aria-label="Illustration of a hand presenting a folded clean shirt with sparkles, set in a water drop"></div>
    <h2 class="screen-title screen-title--single">Receive Your Clean Items</h2>
    <p class="screen-copy screen-copy--three">You’ll be notified that your clothes are ready.<br>Set up a delivery and clean, fresh clothes<br>will be on their way your door.</p>
    <div class="pager"><span class="pager-dot"></span><span class="pager-dot"></span><span class="pager-dot pager-dot--active"></span></div>
    <span class="tour-action">Start</span>
    <span class="home-indicator"></span>
  </section>
</div>
</body>
</html>
```